Website - User Access Door - Images

4 separate images that fit together to form a door that I will animate to open up when a user accesses my website. 1. Left Door 2. Right Door. 3. Lock (open) 4. Lock (closed). High resolution as it must look good on huge monitors.

Attached is a picture very close to what I'm after. I guess the main thing to keep in mind is that it needs to look strong. The attached graphic is quite close to what I'm after, but I need a unique design, not a copy of this one.

Reason: I was promised more than 3 submissions by PixelNook. I guess they need more time...

Here are some images for inspiration. Think Soviet iron nuclear bunker door. Heavy, Strong (but latest technology incorporated)

http://img4.lorvipedia.net/__cb20090716105544/vortra/images/1/1d/KTRF_bunker_door.jpg

http://www.tobiasrenderworks.com/QRT_Bunker3_TobiasKrell.jpg

Nice texture ideas:
http://www.surfacevault.com/data/media/8/steel_door_texture.jpg

Think games:
http://www.stagerundown.com/ironveil/zone7b/24.jpg

http://brightmosaic.com/wp-content/uploads/2013/09/Metal-Door-Wall-Graphic-Decals.jpg

```html
<!DOCTYPE html>
<html lang="en">
<head>
<meta charset="utf-8">
<title>Left Door Panel</title>
<style>
  :root {
    --page-bg: #ffffff;
    --steel-top: #535353;
    --steel-upper: #3c3c3c;
    --steel-mid: #2b2b2b;
    --steel-bottom: #1b1b1b;
    --edge-light: #7a7a7a;
    --edge-dark: #0e0e0e;
  }
  html, body {
    margin: 0;
    padding: 0;
    width: 1200px;
    height: 646px;
    overflow: hidden;
    background: var(--page-bg);
  }
  .door-stage {
    position: relative;
    width: 1200px;
    height: 646px;
  }
  .door-left {
    position: absolute;
    left: 0;
    top: 0;
    width: 1200px;
    height: 646px;
    display: block;
  }
</style>
</head>
<body>
  <main class="door-stage">
    <svg class="door-left" viewBox="0 0 1200 646" role="img" aria-label="Left door panel in dark worn steel with a half-circle lock cut-out on its inner edge">
      <defs>
        <clipPath id="door-shape">
          <path d="M0 0 H607 V169 A151 151 0 0 0 607 471 V646 H0 Z"/>
        </clipPath>

        <linearGradient id="steel-fill" x1="0" y1="0" x2="0" y2="1">
          <stop offset="0" stop-color="var(--steel-top)"/>
          <stop offset="0.22" stop-color="var(--steel-upper)"/>
          <stop offset="0.5" stop-color="var(--steel-mid)"/>
          <stop offset="1" stop-color="var(--steel-bottom)"/>
        </linearGradient>

        <linearGradient id="top-fade" x1="0" y1="0" x2="0" y2="1">
          <stop offset="0" stop-color="#fff" stop-opacity="1"/>
          <stop offset="0.45" stop-color="#fff" stop-opacity="0.35"/>
          <stop offset="1" stop-color="#fff" stop-opacity="0.1"/>
        </linearGradient>
        <mask id="upper-mask">
          <rect width="1200" height="646" fill="url(#top-fade)"/>
        </mask>

        <!-- large cloudy mottling -->
        <filter id="mottle-light" x="0" y="0" width="100%" height="100%">
          <feTurbulence type="fractalNoise" baseFrequency="0.012" numOctaves="5" seed="4"/>
          <feColorMatrix type="matrix" values="0 0 0 0 1  0 0 0 0 1  0 0 0 0 1  0.7 0 0 0 -0.36"/>
        </filter>
        <filter id="mottle-dark" x="0" y="0" width="100%" height="100%">
          <feTurbulence type="fractalNoise" baseFrequency="0.015" numOctaves="5" seed="11"/>
          <feColorMatrix type="matrix" values="0 0 0 0 0  0 0 0 0 0  0 0 0 0 0  -0.8 0 0 0 0.36"/>
        </filter>

        <!-- fine grain -->
        <filter id="grain" x="0" y="0" width="100%" height="100%">
          <feTurbulence type="fractalNoise" baseFrequency="0.85" numOctaves="2" seed="7"/>
          <feColorMatrix type="matrix" values="0 0 0 0 1  0 0 0 0 1  0 0 0 0 1  0.9 0 0 0 -0.42"/>
        </filter>
        <filter id="grain-dark" x="0" y="0" width="100%" height="100%">
          <feTurbulence type="fractalNoise" baseFrequency="0.7" numOctaves="2" seed="19"/>
          <feColorMatrix type="matrix" values="0 0 0 0 0  0 0 0 0 0  0 0 0 0 0  -1 0 0 0 0.55"/>
        </filter>

        <!-- brushed scratches -->
        <filter id="brushed" x="0" y="0" width="100%" height="100%">
          <feTurbulence type="fractalNoise" baseFrequency="0.006 0.6" numOctaves="3" seed="3"/>
          <feColorMatrix type="matrix" values="0 0 0 0 1  0 0 0 0 1  0 0 0 0 1  1.4 0 0 0 -0.78"/>
        </filter>

        <linearGradient id="edge-bevel" x1="0" y1="0" x2="1" y2="0">
          <stop offset="0" stop-color="#000" stop-opacity="0"/>
          <stop offset="0.7" stop-color="#000" stop-opacity="0.25"/>
          <stop offset="1" stop-color="#000" stop-opacity="0.55"/>
        </linearGradient>
      </defs>

      <g class="door-panel" clip-path="url(#door-shape)">
        <rect class="steel-base" width="607" height="646" fill="url(#steel-fill)"/>
        <rect class="steel-mottle-light" width="607" height="646" filter="url(#mottle-light)" mask="url(#upper-mask)"/>
        <rect class="steel-mottle-dark" width="607" height="646" filter="url(#mottle-dark)"/>
        <rect class="steel-grain" width="607" height="646" filter="url(#grain)" opacity="0.55"/>
        <rect class="steel-grain-dark" width="607" height="646" filter="url(#grain-dark)" opacity="0.6"/>
        <g class="steel-brushing" mask="url(#upper-mask)" opacity="0.5">
          <rect x="-300" y="-300" width="1400" height="1300" filter="url(#brushed)" transform="rotate(-28 300 320)"/>
        </g>
        <rect class="edge-shade" x="590" y="0" width="17" height="646" fill="url(#edge-bevel)"/>
      </g>

      <path class="door-edge"
            d="M606 0 V169 A151 151 0 0 0 606 471 V646"
            fill="none" stroke="var(--edge-dark)" stroke-width="3"/>
      <path class="lock-rim-upper"
            d="M604 169 A151 151 0 0 0 456 320"
            fill="none" stroke="#000" stroke-width="4" stroke-opacity="0.6"/>
      <path class="lock-rim-lower"
            d="M470 390 A151 151 0 0 0 604 471"
            fill="none" stroke="var(--edge-light)" stroke-width="3"/>
    </svg>
  </main>
</body>
</html>
```